New business card for my lawn and landscape business

Dorrin Yard and Building is a full-service lawn care, landscaping, and light construction company serving Paragould and the Northeast Arkansas region. The business is owned and operated by Marcus Toller, with a reputation for hands-on, detail-oriented service, dependable crews, and quality results for both residential and commercial clients. A well regarded business with great reviews.
Owner Marcus Toller
Dorrinyardandbuilding.example

Target Market(s)

Commercial, Middle, and upper class in north east Arkansas

Industry/Entity Type

Lawn maintenance and landscape

Contact Information for Business Card

Dorrin Yard And Building Professional lawn care, landscaping, and property improvement in Northeast Arkansas. • lawn maintenance •lawn treatments and weed control • exterior projects • Custom landscape design & installation • Sod, trees, rock & drainage solutions • Residential & commercial services Reliable. Detailed. Done right.

Requirements
Must have
• Business name, service area, list of some of our services, clean design that represents
Nice to have
• Unique. Different design element than just grass because its already in n the logo. Picture of a warm season (south) lawn or landscape. Pictures of the type of work we do

```html
<!DOCTYPE html>
<html lang="en">
<head>
<meta charset="utf-8">
<title>Dorrin Yard and Building – Business Card</title>
<link href="https://fonts.googleapis.com/css2?family=Montserrat:wght@400;500;600;700&display=swap" rel="stylesheet">
<style>
  :root{
    --bg:#9a9a9a;
    --card-dark:#151516;
    --card-light:#ffffff;
    --green:#76b043;
    --ink:#1e1e1e;
    --muted:#6b6b6b;
    --steel:#cfcfcf;
    --steel-dim:#8a8a8a;
  }
  *{margin:0;padding:0;box-sizing:border-box}
  html,body{width:1200px;height:1108px;overflow:hidden;background:var(--bg);font-family:"Montserrat",sans-serif}
  .card{position:absolute;left:242px;width:715px;height:409px}
  .card-front{
    top:119px;
    background:linear-gradient(125deg,var(--card-dark) 0%,var(--card-dark) 30%,#3a3a3c 46%,#262627 62%,var(--card-dark) 85%);
    display:flex;align-items:center;justify-content:center;gap:18px;
  }
  .front-mark{width:56px;height:56px;border-radius:50%;border:3px solid var(--steel-dim)}
  .front-name{font-weight:600;font-size:34px;letter-spacing:1px;color:var(--steel);line-height:1.15}
  .card-back{top:580px;background:var(--card-light)}
  .back-brand{position:absolute;left:44px;top:126px;width:228px;height:157px;display:flex;align-items:center;gap:12px}
  .brand-mark{flex:none;width:34px;height:34px;border-radius:50%;border:3px solid var(--steel-dim)}
  .brand-name{font-weight:600;font-size:25px;line-height:1.15;color:var(--green)}
  .service-area{font-weight:500;font-size:12px;line-height:1.35;color:var(--muted);margin-top:8px;letter-spacing:.3px}
  .divider{position:absolute;left:285px;top:126px;width:2px;height:157px;background:var(--green)}
  .contact{position:absolute;left:314px;top:118px}
  .person-name{font-weight:700;font-size:33px;color:var(--green);line-height:1.1}
  .person-role{font-weight:500;font-size:18px;color:var(--ink);margin-top:6px;letter-spacing:.5px}
  .contact-list{list-style:none;margin-top:20px}
  .contact-list li{display:flex;align-items:center;gap:8px;font-size:17px;font-weight:500;color:var(--ink);height:28px}
  .contact-list svg{width:16px;height:16px;flex:none}
  .services{position:absolute;left:30px;right:30px;top:304px;text-align:center;font-size:17px;font-weight:500;line-height:28px;color:var(--ink)}
</style>
</head>
<body>
  <section class="card card-front" aria-label="Card front">
    <span class="front-mark"></span>
    <span class="front-name">Dorrin Yard and Building</span>
  </section>

  <section class="card card-back" aria-label="Card back">
    <div class="back-brand">
      <span class="brand-mark"></span>
      <div>
        <span class="brand-name">Dorrin Yard<br>and Building</span>
        <p class="service-area">Serving Paragould &amp;<br>Northeast Arkansas</p>
      </div>
    </div>
    <div class="divider"></div>
    <div class="contact">
      <h1 class="person-name">Marcus Toller</h1>
      <p class="person-role">Owner</p>
      <ul class="contact-list">
        <li>
          <svg viewBox="0 0 16 16" aria-hidden="true"><path fill="#76b043" d="M1 6c0-2 3-3 7-3s7 1 7 3v1h-3V5.5C11 5 9.5 4.8 8 4.8S5 5 4 5.5V7H1zM3 8h10l1 6H2z"/></svg>
          123 456 789
        </li>
        <li>
          <svg viewBox="0 0 16 16" aria-hidden="true"><rect x="1" y="3" width="14" height="10" fill="#76b043"/><path d="M1 3l7 6 7-6" fill="none" stroke="#fff" stroke-width="1.4"/></svg>
          info@Dorrinyardandbuilding.example
        </li>
        <li>
          <svg viewBox="0 0 16 16" aria-hidden="true"><circle cx="8" cy="8" r="7" fill="#76b043"/><path d="M4 5c2 0 3 1 2 3s1 3 2 4M10 3c0 2 2 2 3 3" fill="none" stroke="#fff" stroke-width="1.3"/></svg>
          Dorrinyardandbuilding.example
        </li>
      </ul>
    </div>
    <p class="services">lawn maintenance •lawn treatments and weed control • exterior projects •<br>Custom landscape design &amp; installation • Sod, trees, rock &amp; drainage solu-<br>tions • Residential &amp; commercial services Reliable. Detailed. Done right.</p>
  </section>
</body>
</html>
```